Driving-coach/trainer who wants to inform about the offer and how I can help people to drive more re

I need a flyer that informs potential customers about my offer.

DL size 210 mm x 99 mm, vertical!

I'm a trainer/coach who helps people to drive a car more relaxed, without fear and more confident.

It's a one to one training. I do train people in their own car. It gets people their freedom back to go where and when they like to go by own car...

Target Market(s)

People (man an woman) who are afraid of driving a car, or are very stressed while driving....

Industry/Entity Type

Life Coaching

Font styles to use
Sans Serif

Colors
acd136

Requirements
Must have
• Page 1:
• -my offer (see text-pdf)
• -three fotos (see attached files "Pixmarra") of people who are satisfied with my offer
• Page 2:
• -advantages in the work with me.
• -contact information
• -and a picture of me (see attached file) next to the contact information or the advantages of my work
• -my logo (see attached file) on Page 1 + 2
• -i like a "clear" and structured layout. "Less is more"

```html
<!DOCTYPE html>
<html lang="de">
<head>
<meta charset="utf-8">
<title>Fahrangst-Coach Flyer</title>
<link rel="stylesheet" href="https://fonts.googleapis.com/css2?family=Oswald:wght@500&family=Roboto:wght@400&family=Roboto+Condensed:wght@400;700&family=Russo+One&family=Ubuntu:wght@400&display=swap">
<style>
:root{
  --green:#acd136;
  --green-deep:#6fa52a;
  --green-text:#7cbb3a;
  --black:#121212;
  --dark:#1d1d1d;
  --white:#ffffff;
  --bg:#d9d9d6;
}
*{margin:0;padding:0;box-sizing:border-box}
html,body{width:1200px;height:1198px;overflow:hidden;background:var(--bg)}
.flyer{position:absolute;top:37px;width:540px;height:1081px;overflow:hidden;background:var(--black);font-family:"Roboto Condensed",sans-serif;color:var(--white);box-shadow:0 4px 14px rgba(0,0,0,.35)}
.flyer.front{left:34px}
.flyer.back{left:625px}
.shapes{position:absolute;inset:0}
.abs{position:absolute}
.hero-photo{left:0;top:0;width:540px;height:420px;clip-path:path('M0 0 H540 V265 Q450 380 300 390 Q120 398 0 335 Z');background:linear-gradient(135deg,#aabd7a,#d8b59c 55%,#8a7c5f)}
.hero-box{left:12px;top:0;width:295px;height:343px;background:rgba(140,190,40,.72)}
.hero-title{left:20px;top:8px;font-family:"Oswald",sans-serif;font-size:66px;line-height:1;letter-spacing:.5px}
.hero-q{left:37px;font-family:"Roboto",sans-serif;font-size:21.5px;line-height:26px}
.hero-cta{left:12px;top:280px;width:295px;text-align:center;font-family:"Russo One",sans-serif;font-size:20px;line-height:27px;letter-spacing:1.5px}
.heading{font-family:"Russo One",sans-serif;font-size:21px;letter-spacing:2.6px;line-height:27px;font-weight:400}
.heading .accent{color:var(--green-text)}
.checks{list-style:none;font-size:15.5px;line-height:18.5px}
.checks li{position:relative;padding-left:24px;margin-bottom:10px}
.checks svg{position:absolute;left:2px;top:2px;width:15px;height:13px}
.portrait{left:348px;top:697px;width:138px;height:138px;border-radius:50%;border:4px solid var(--white);background:radial-gradient(circle at 50% 40%,#f2f2f2,#b9bcc2);box-shadow:0 3px 10px rgba(0,0,0,.6)}
.subline{left:27px;top:782px;font-size:21px;line-height:26px;color:var(--green-text)}
.steps-title{left:27px;top:815px;font-family:"Russo One",sans-serif;font-size:21px;line-height:28px;letter-spacing:2px}
.step{width:130px;height:130px;border-radius:50%;border:4px solid var(--white);background:#1a1a1a;display:flex;flex-direction:column;align-items:center;justify-content:center;text-align:center;box-shadow:0 3px 8px rgba(0,0,0,.6)}
.step.active{border-color:var(--green-deep)}
.step .num{font-family:"Oswald",sans-serif;font-size:28px;color:var(--green-text);line-height:30px}
.step .txt{font-size:16px;line-height:20px}
.step.active .txt{font-size:14px;line-height:17.5px}
.footer{left:0;top:996px;width:540px;height:85px;background:var(--white);border-top:4px solid var(--green-deep);border-bottom:4px solid var(--green-deep)}
.brand-name{font-family:"Ubuntu",sans-serif;color:var(--green-text);letter-spacing:4px}
.footer .brand-name{position:absolute;left:34px;top:8px;font-size:33px}
.footer .brand-role{position:absolute;left:34px;top:49px;font-family:"Ubuntu",sans-serif;font-size:23px;letter-spacing:3px;color:var(--green-text)}
.back-photo{left:0;top:0;width:540px;height:400px;background:linear-gradient(180deg,#d4d4d4,#9a9a9a 55%,#6f6f6f)}
.cabrio-photo{left:285px;top:715px;width:255px;height:208px;background:linear-gradient(135deg,#c9b49a,#8b6a47 60%,#3c3a36);clip-path:polygon(60% 0,100% 0,100% 100%,0 55%)}
.back .checks{font-size:16.5px;line-height:18px}
.contact{left:0;width:540px;text-align:center;font-size:19px}
.contact.info{font-family:"Ubuntu",sans-serif;font-size:20px;letter-spacing:2px;color:var(--green-text)}
</style>
</head>
<body>

<section class="flyer front">
  <svg class="shapes" viewBox="0 0 540 1081" aria-hidden="true">
    <path d="M0 380 Q200 440 330 420 Q450 400 540 320 V1081 H0 Z" fill="#1a1a1a"/>
    <path d="M0 740 L348 790 L540 700 V1081 H0 Z" fill="#232323"/>
    <path d="M0 700 L330 782" stroke="#acd136" stroke-width="2"/>
    <path d="M330 782 L352 787" stroke="#d4c21c" stroke-width="2"/>
    <path d="M488 775 L540 742" stroke="#acd136" stroke-width="2"/>
  </svg>
  <div class="abs hero-photo" role="img" aria-label="Foto: lächelnde Fahrerin im Auto, Daumen hoch"></div>
  <svg class="shapes" viewBox="0 0 540 1081" aria-hidden="true">
    <defs>
      <linearGradient id="swoosh" x1="0" y1="0" x2="1" y2="0">
        <stop offset="0" stop-color="#4f8a1c"/>
        <stop offset=".5" stop-color="#acd136"/>
        <stop offset="1" stop-color="#5e9a22"/>
      </linearGradient>
    </defs>
    <path d="M0 335 Q120 398 300 390 Q450 380 540 265 V290 Q440 410 290 415 Q110 420 0 352 Z" fill="#0e0e0e"/>
    <path d="M0 352 Q110 420 290 415 Q440 410 540 290 V300 Q450 425 300 432 Q120 438 0 375 Z" fill="url(#swoosh)"/>
  </svg>

  <div class="abs hero-box"></div>
  <div class="abs hero-title">Wollen Sie</div>
  <div class="abs hero-q" style="top:90px">Fahrangst überwinden?</div>
  <div class="abs hero-q" style="top:127px">Panikattacken beim<br>Autofahren loswerden?</div>
  <div class="abs hero-q" style="top:190px">Oder einfach sicher<br>Autofahren?</div>
  <div class="abs hero-cta">DANN SIND SIE HIER<br>RICHTIG!</div>

  <h2 class="abs heading" style="left:29px;top:420px">KOMMT IHNEN EINE DIESER<br><span class="accent">SITUATIONEN BEKANNT VOR?</span></h2>

  <ul class="abs checks" style="left:28px;top:494px;width:478px">
    <li><svg viewBox="0 0 15 13"><path d="M1 7 L5 11 L14 1" stroke="#7cbb3a" stroke-width="2.6" fill="none"/></svg>Angst oder Panikattacken begleiten Sie beim Autofahren. Vielleicht vermeiden Sie deshalb das Autofahren komplett. - Sie möchten angstfrei und/oder ohne Panikattacken fahren.</li>
    <li><svg viewBox="0 0 15 13"><path d="M1 7 L5 11 L14 1" stroke="#7cbb3a" stroke-width="2.6" fill="none"/></svg>Sie trauen sich das Autofahren nicht (mehr) zu. - Sie wünschen sich, sicher, entspannt und stressfrei Auto zu fahren.</li>
    <li><svg viewBox="0 0 15 13"><path d="M1 7 L5 11 L14 1" stroke="#7cbb3a" stroke-width="2.6" fill="none"/></svg>Autofahren erleben Sie unter hoher Anspannung und Stress. - Sie wünschen sich, Autofahren sicher und entspannt zu erleben.</li>
    <li><svg viewBox="0 0 15 13"><path d="M1 7 L5 11 L14 1" stroke="#7cbb3a" stroke-width="2.6" fill="none"/></svg>Bestimmte Situationen (z.B. Autobahn, Baustellen, Stadtverkehr...) bereiten Ihnen großen Stress. - Sie möchten diese Situationen souveräner meistern.</li>
  </ul>

  <div class="abs portrait" role="img" aria-label="Porträtfoto der Trainerin in weißer Bluse"></div>
  <div class="abs subline">Das muss nicht so bleiben!</div>
  <div class="abs steps-title">3 SCHRITTE ZUR LÖSUNG:</div>

  <div class="abs step" style="left:38px;top:856px"><span class="num">1.</span><span class="txt">Erstgespräch<br>vereinbaren</span></div>
  <div class="abs step active" style="left:211px;top:856px"><span class="num">2.</span><span class="txt">Analyse Ihrer<br>individuellen<br>Situation und<br>Zielsetzung</span></div>
  <div class="abs step" style="left:380px;top:856px"><span class="num">3.</span><span class="txt">Individuelles<br>Coaching<br>und Training</span></div>

  <div class="abs footer">
    <div class="brand-name">Katrin Vollmer</div>
    <div class="brand-role">Fahrangst-Bewältigungs-Coach</div>
  </div>
</section>

<section class="flyer back">
  <div class="abs back-photo" role="img" aria-label="Schwarzweißfoto: Kleinwagen mit Koffern auf dem Dach in einer Wiese"></div>
  <svg class="shapes" viewBox="0 0 540 1081" aria-hidden="true">
    <defs>
      <linearGradient id="swooshB" x1="0" y1="0" x2="1" y2="0">
        <stop offset="0" stop-color="#5e9a22"/>
        <stop offset=".5" stop-color="#acd136"/>
        <stop offset="1" stop-color="#4f8a1c"/>
      </linearGradient>
    </defs>
    <path d="M0 240 Q100 290 170 340 Q260 395 380 395 Q480 390 540 325 V1081 H0 Z" fill="#0e0e0e"/>
    <path d="M0 240 Q90 285 150 330 Q240 395 380 405 Q480 400 540 325 V345 Q470 410 370 414 Q240 410 140 345 Q80 300 0 260 Z" fill="url(#swooshB)"/>
    <path d="M0 420 Q120 330 260 410 Q380 470 540 400 V1081 H0 Z" fill="#171717"/>
    <path d="M0 739 L108 810 L540 700 V1081 H0 Z" fill="#222"/>
    <path d="M0 739 L108 810 L540 700" stroke="#acd136" stroke-width="2" fill="none"/>
    <path d="M108 810 L150 800" stroke="#d4c21c" stroke-width="2"/>
  </svg>
  <div class="abs cabrio-photo" role="img" aria-label="Foto: lächelnde ältere Fahrerin im Cabrio"></div>

  <h2 class="abs heading" style="left:29px;top:408px;letter-spacing:3px"><span class="accent">ADVANTAGES</span><br>IN THE WORK WITH ME:</h2>

  <ul class="abs checks" style="left:29px;top:478px;width:482px">
    <li><svg viewBox="0 0 15 13"><path d="M1 7 L5 11 L14 1" stroke="#7cbb3a" stroke-width="2.6" fill="none"/></svg>über 10 Jahre Erfahrung als Trainerin und Coach im Bereich Fahrsicherheit.</li>
    <li><svg viewBox="0 0 15 13"><path d="M1 7 L5 11 L14 1" stroke="#7cbb3a" stroke-width="2.6" fill="none"/></svg>Als psychotherapeutische Heilpraktikerin bin ich auf Angststörungen und Panikattacken spezialisiert</li>
    <li><svg viewBox="0 0 15 13"><path d="M1 7 L5 11 L14 1" stroke="#7cbb3a" stroke-width="2.6" fill="none"/></svg>100 % auf Sie zugeschnitten: ich hole Sie genau dort ab, wo Sie jetzt stehen und unterstütze Sie in Ihrem Prozess individuell und zielführend.</li>
    <li><svg viewBox="0 0 15 13"><path d="M1 7 L5 11 L14 1" stroke="#7cbb3a" stroke-width="2.6" fill="none"/></svg>Wenn es Ihnen nicht möglich ist, in meine Praxis nach Neustadt Süd zu kommen: Mit der mobilen Praxis komme ich auch zu Ihnen.</li>
    <li><svg viewBox="0 0 15 13"><path d="M1 7 L5 11 L14 1" stroke="#7cbb3a" stroke-width="2.6" fill="none"/></svg>Termine sind auch abends und am Wochenende möglich.</li>
  </ul>

  <div class="abs contact brand-name" style="top:908px;font-size:34px">Katrin Vollmer</div>
  <div class="abs contact info" style="top:950px">Weitere Informationen finden Sie auf:</div>
  <div class="abs contact" style="top:982px">www.angstfrei-fahren-coaching.de</div>
  <div class="abs contact" style="top:1012px">Oder rufen Sie mich einfach an:</div>
  <div class="abs contact" style="top:1042px">Tel. 0160 47 31 88 25</div>
</section>

</body>
</html>
```